DOUBLE SIDED BROCHURE NEEDED TO PROMOTE DOCTOR

I need a double sided DL size (99mm x 210mm) brochure, promoting a doctor seeing patients in a new area.

I want something professional. I have included the relevant information. I would also like the Dr's picture somwhere in the brochure, with a professional background. I wish to print these tomorrow, so i will pick a winner within 14 hours of posting this ad.

I have included an example of a brochures design that I recently saw, and its definietly a good starting point.

Medical

```html
<!DOCTYPE html>
<html lang="en">
<head>
<meta charset="utf-8">
<title>Dr. Haddad – Referral Brochure</title>
<link rel="stylesheet" href="https://fonts.googleapis.com/css2?family=Jost:wght@400;500;600;700&display=swap">
<style>
  :root {
    --stage: #e4e5e8;
    --navy: #28246e;
    --ink: #1e1b4f;
    --sky: #1ea6e6;
    --paper-top: #e8f3fa;
    --paper-bottom: #f7fbfe;
    --white: #ffffff;
  }
  * { margin: 0; padding: 0; box-sizing: border-box; }
  html, body { width: 1200px; height: 1200px; overflow: hidden; }
  body { background: var(--stage); position: relative; font-family: "Jost", Arial, sans-serif; color: var(--ink); }

  .panel {
    position: absolute; top: 84px; width: 416px; height: 882px;
    transform: scale(1.2); transform-origin: 0 0;
    background: linear-gradient(180deg, var(--paper-top), var(--paper-bottom));
    overflow: hidden;
  }
  .panel--front { left: 62px; }
  .panel--back { left: 635px; }
  .panel__art { position: absolute; inset: 0; width: 416px; height: 882px; }
  .panel__text { position: absolute; }

  .letter { left: 17px; top: 424px; width: 390px; font-size: 15px; line-height: 25.5px; }
  .letter strong { color: var(--navy); font-weight: 600; }

  .contact { position: absolute; left: 0; width: 416px; text-align: center; color: var(--white); font-weight: 600; line-height: 1; }
  .contact__label { font-size: 24px; }
  .contact__number { font-size: 26px; margin-top: 8px; }
  .panel--front .contact { top: 714px; }
  .panel--back .contact { top: 800px; }
  .panel--back .contact__label { font-size: 28px; }
  .panel--back .contact__number { font-size: 32px; }

  .clinic { left: 20px; top: 817px; color: var(--white); font-size: 13px; line-height: 16px; }
  .clinic b { font-size: 15px; font-weight: 600; display: block; }
  .referrals { left: 200px; top: 831px; color: var(--white); font-size: 14px; line-height: 21px; text-align: right; width: 200px; }

  .title { left: 20px; top: 116px; }
  .title__name { font-size: 37px; font-weight: 700; color: var(--navy); line-height: 1; }
  .title__line { font-size: 20px; font-weight: 500; color: var(--ink); line-height: 1; margin-top: 6px; }
  .title__sub { font-size: 13.5px; font-weight: 700; color: var(--ink); margin-top: 7px; line-height: 1; }

  .intro { left: 22px; top: 422px; width: 380px; font-size: 13.5px; line-height: 19px; }
  .intro b { font-weight: 700; }
  .group-title { left: 22px; top: 596px; font-size: 13px; font-weight: 700; }
  .group-title span { font-weight: 400; }

  .service { position: absolute; font-size: 12.5px; line-height: 15px; padding-left: 21px; }
  .service::before {
    content: "+"; position: absolute; left: 0; top: 0; width: 14px; height: 14px;
    background: var(--navy); color: var(--white); font-size: 14px; line-height: 13px;
    text-align: center; font-weight: 700;
  }
  .service small { display: block; font-size: 10px; line-height: 12px; padding-left: 4px; }
</style>
</head>
<body>

<!-- Front panel -->
<section class="panel panel--front">
  <svg class="panel__art" viewBox="0 0 416 882" aria-hidden="false">
    <defs>
      <linearGradient id="hospitalTone" x1="0" y1="0" x2="0" y2="1">
        <stop offset="0" stop-color="#3b79c4"/>
        <stop offset="0.45" stop-color="#8fa6bd"/>
        <stop offset="1" stop-color="#6d7680"/>
      </linearGradient>
    </defs>
    <path role="img" aria-label="Photo of the hospital building" fill="url(#hospitalTone)"
          d="M0 0 H416 V300 C300 345 170 330 0 235 Z"/>
    <path fill="var(--sky)" d="M0 225 C140 340 300 350 416 262 V300 C300 385 130 375 0 262 Z"/>
    <path fill="var(--white)" d="M0 262 C130 375 300 385 416 300 V308 C300 392 130 382 0 270 Z"/>
    <path fill="var(--navy)" d="M0 270 C130 382 300 392 416 308 V330 C290 430 110 430 0 312 Z"/>

    <path fill="var(--sky)" d="M0 728 C110 650 310 645 416 718 V882 H0 Z"/>
    <path fill="var(--white)" d="M0 742 C110 668 310 663 416 734 V882 H0 Z"/>
    <path fill="var(--navy)" d="M0 750 C110 678 310 673 416 742 V882 H0 Z"/>
    <rect x="20" y="770" width="40" height="40" fill="#ffffff" opacity="0.05"/>
    <rect x="350" y="760" width="50" height="50" fill="#ffffff" opacity="0.05"/>

    <circle cx="206" cy="684" r="17" fill="var(--navy)" stroke="var(--white)" stroke-width="2"/>
    <path fill="var(--white)" d="M199 676 c2-2 4-1 5 1 l2 3 c1 2 0 3-1 4 c1 3 3 5 6 6 c1-1 2-2 4-1 l3 2 c2 1 2 3 1 4 c-2 3-5 4-9 2 c-5-3-9-7-12-12 c-2-4-1-7 1-9 Z"/>

    <circle cx="86" cy="802" r="10" fill="none" stroke="var(--white)" stroke-width="1.2" opacity="0.8"/>
    <path fill="var(--white)" d="M86 795 c-3 0-5 2-5 5 c0 4 5 9 5 9 s5-5 5-9 c0-3-2-5-5-5 Z M86 798 a2 2 0 1 1 0 4 a2 2 0 1 1 0-4 Z" fill-rule="evenodd"/>

    <g fill="var(--white)">
      <rect x="222" y="856" width="6" height="13" rx="1"/>
      <rect x="229" y="859" width="11" height="10" rx="1"/>
      <rect x="231" y="853" width="7" height="5"/>
    </g>
  </svg>

  <p class="panel__text letter">
    Dear Doctors,<br>
    We are pleased to announce that <strong>Dr.SamirHaddad</strong><br>
    is now consulting in Seabrook, seeing public<br>
    and private patients.<br>
    Guaranteed appointment within two weeks,<br>
    with patients having the option of surgery at<br>
    Coastal Health Campus, Harbourview Hospital<br>
    or St. Brigid's Riverside.
  </p>

  <div class="contact">
    <div class="contact__label">CONTACT US</div>
    <div class="contact__number">1300 555 014</div>
  </div>

  <p class="panel__text clinic"><b>Seabrook Clinic:</b>42 Kestrel Road<br>Seabrook WA 6999.</p>
  <p class="panel__text referrals">Please send all referrals by<br>(08) 5550 1427.</p>
</section>

<!-- Back panel -->
<section class="panel panel--back">
  <svg class="panel__art" viewBox="0 0 416 882">
    <defs>
      <linearGradient id="portraitTone" x1="0" y1="0" x2="0" y2="1">
        <stop offset="0" stop-color="#c7ccd3"/>
        <stop offset="0.55" stop-color="#8d8a90"/>
        <stop offset="1" stop-color="#2f3140"/>
      </linearGradient>
    </defs>
    <path role="img" aria-label="Portrait photo of the surgeon" fill="url(#portraitTone)"
          d="M171 10 H416 V320 H171 Z"/>
    <path fill="var(--sky)" d="M0 205 C120 330 300 360 416 262 V292 C300 390 120 365 0 238 Z"/>
    <path fill="var(--white)" d="M0 238 C120 365 300 390 416 292 V300 C300 398 120 373 0 246 Z"/>
    <path fill="var(--navy)" d="M0 246 C120 373 300 398 416 300 V338 C300 440 110 430 0 290 Z"/>

    <path fill="var(--sky)" d="M0 820 C90 745 320 735 416 805 V882 H0 Z"/>
    <path fill="var(--white)" d="M0 836 C90 762 320 752 416 822 V882 H0 Z"/>
    <path fill="var(--navy)" d="M0 844 C90 772 320 762 416 830 V882 H0 Z"/>

    <circle cx="208" cy="768" r="20" fill="var(--navy)" stroke="var(--white)" stroke-width="2"/>
    <path fill="var(--white)" d="M200 758 c2-2 5-1 6 1 l2 4 c1 2 0 3-1 4 c1 3 4 6 7 7 c1-1 2-2 4-1 l4 2 c2 1 2 4 1 5 c-2 3-6 4-10 2 c-6-3-11-8-14-14 c-2-4-1-8 1-10 Z"/>
  </svg>

  <div class="panel__text title">
    <div class="title__name">Dr.Haddad</div>
    <div class="title__line">HIGHLY TRAINED</div>
    <div class="title__sub">SPECIALISED SURGEON</div>
  </div>

  <p class="panel__text intro"><b>Dr.Haddad</b> is a highly trained specialised surgeon, in all areas of Endocrine, Breast and General Surgery. Including;</p>

  <p class="service" style="left:22px; top:501px;">Thyroid Surgery</p>
  <p class="service" style="left:207px; top:501px;">Parathyroid surgery<small>(including minimally<br>&nbsp;invasive parathyroidectomy)</small></p>
  <p class="service" style="left:22px; top:555px;">Breast Cancer</p>
  <p class="service" style="left:207px; top:555px;">Benign breast lesions</p>

  <p class="panel__text group-title">All areas of general surgery, <span>such as;</span></p>

  <p class="service" style="left:22px; top:630px;">Gallbladder surgery</p>
  <p class="service" style="left:207px; top:630px;">Carpal Tunnel</p>
  <p class="service" style="left:22px; top:667px;">Hernia surgery</p>
  <p class="service" style="left:207px; top:667px;">Vasectomy etc…</p>
  <p class="service" style="left:22px; top:704px;">Haemorrhoids</p>

  <div class="contact">
    <div class="contact__label">CONTACT US</div>
    <div class="contact__number">1300 555 014</div>
  </div>
</section>

</body>
</html>
```